Guaranteed Job - Sleek Sexy Business Card UV Spot

Im looking for a sleek and sexy business card, that resembles elite or VIP status status.
our business is corinvale.example
you can view our products on there, but our main audience for handing out our cards will be for people in the hospitality industry, so it will need to impress high management and CEO of hotels and restaurants, bars, clubs etc...
the card features will have UV spot on both sides, 400gsm stock. standard size.
Artwork should be 86 x 54mm + 2mm bleed = 90 x 58mm
it should have a nice "unique" uv spot pattern that highlights the card, not a repeated pattern, theres no originality there, and it will be disregarded.
The written material will be:
Corin Vale Hospitality College (logo)
Tobin Marsh
Director
Phone: 1300 615 737
Mobile: 0455 817 296
Email: info@corinvale.example
website: www.corinvale.example
I'm looking for originality here, i don't want just a simple stock card, want something that has a wow factor for people.
You will find the logo attached. you may invert the white to black words to suit the background as you please.
thank you and good luck
As a side note, ive received a lot of proposals, im too busy to give feedback to each and every one, so if i havent provided feedback for your design within 24 hours, then consider it not acceptable, and you could resubmit another design.
So far i have not seen any design that stood out for me, they all seem pretty generic. there nothing thats unique, i would figure for the amount that im offering, that people would put some more effort and creativity into the design.
so far over 200 designs submitted, and nothing i have seen looks very original, everything looks like a different variation of the same stuff, i said it very clearly i wanted something unique, the only thing that has come close to it so far is this one
Reason: Ive received alot of design concepts and i have reviewed everyone, but i havent had time to give feedback to every single one, only the ones that have interested me, if i havent responded, its because i havent found it good enough.
so far only a few design have been on par with what ive been looking for, an attractive eye popping design.
heres a few of them,
http://files.pixelbazaar.example/design_img/51736/62418/62418_2840915_51736_image.jpg
http://files.pixelbazaar.example/design_img/51736/68254/68254_2841377_51736_image.jpg
theyre, both unique and original, and eye catching, the only thing theyre missing is the sexyness.
if you still think you have some creativity left in your minds, then throw it on here.
Reason: Sorry guys for the delay, I was in a serious accident and out of commission for the past few months, I'm just slowly recovering now, please bare with me as i try to attend to this project, it may take me awhile as I have other projects that are on standby, I'm not 100% at the moment, so im extending the deadline for 2 weeks right now. Thanks for your patience.
Hospitality

```html
<!DOCTYPE html>
<html lang="en">
<head>
<meta charset="utf-8">
<title>Corin Vale Hospitality College – Business Card</title>
<link rel="stylesheet" href="https://fonts.googleapis.com/css2?family=Source+Sans+3:wght@400;600&family=Arimo:wght@400&display=swap">
<style>
  :root {
    --board: #4a4df2;
    --card: #29292b;
    --card-edge: #b9b9bd;
    --accent: #5cc7f2;
    --accent-soft: #7fd2f2;
    --name: #f4e6ea;
  }
  * { margin: 0; padding: 0; box-sizing: border-box; }
  html, body {
    width: 1200px;
    height: 1200px;
    overflow: hidden;
    background: var(--board);
  }
  .board { position: relative; width: 1200px; height: 1200px; }

  .card {
    position: absolute;
    width: 899px;
    height: 574px;
    background: var(--card);
    border: 2px solid var(--card-edge);
    overflow: hidden;
    transform-origin: top left;
  }
  .card--main { left: 144px; top: 37px; }
  .card--small-left { left: 37px; top: 646px; transform: scale(0.595); }
  .card--small-right { left: 593px; top: 650px; transform: scale(0.595); }

  .card__swoosh { position: absolute; inset: 0; width: 100%; height: 100%; }

  .brand {
    position: absolute;
    left: 268px;
    top: 18px;
    display: flex;
    align-items: center;
    gap: 14px;
    color: var(--accent);
    font-family: "Source Sans 3", sans-serif;
    font-weight: 600;
  }
  .brand__dot {
    width: 58px; height: 58px;
    border-radius: 50%;
    background: var(--accent);
  }
  .brand__name { line-height: 1; text-transform: uppercase; }
  .brand__line { display: block; font-size: 34px; letter-spacing: 1px; }
  .brand__sub { display: block; font-size: 13px; letter-spacing: 1.5px; margin-top: 4px; }

  .person {
    position: absolute;
    left: 0;
    width: 816px;
    top: 192px;
    text-align: center;
    color: var(--name);
    font-family: "Source Sans 3", sans-serif;
    font-weight: 400;
  }
  .person__name { font-size: 56px; line-height: 1.05; }
  .person__role { font-size: 46px; line-height: 1.1; }

  .contact {
    position: absolute;
    color: var(--accent-soft);
    font-family: "Arimo", sans-serif;
    font-size: 32px;
    line-height: 50px;
  }
  .contact--phones { left: 16px; top: 342px; }
  .contact--online { right: 30px; top: 470px; text-align: right; }
</style>
</head>
<body>
<main class="board">

  <article class="card card--main">
    <svg class="card__swoosh" viewBox="0 0 899 574" aria-hidden="true">
      <path d="M0,300 Q340,-10 895,300 Q350,40 0,312 Z" fill="var(--accent)"/>
      <path d="M0,500 Q150,500 292,452 Q140,482 0,478 Z" fill="var(--accent)"/>
    </svg>
    <div class="brand">
      <span class="brand__dot"></span>
      <span class="brand__name">
        <span class="brand__line">Corin Vale</span>
        <span class="brand__sub">Hospitality College</span>
      </span>
    </div>
    <div class="person">
      <p class="person__name">Tobin Marsh</p>
      <p class="person__role">Director</p>
    </div>
    <div class="contact contact--phones">
      <p>Phone : 1300 615 737</p>
      <p>Mobile : 0455 817 296</p>
    </div>
    <div class="contact contact--online">
      <p>Email : info@corinvale.example</p>
      <p>Website : www.corinvale.example</p>
    </div>
  </article>

  <article class="card card--small-left">
    <svg class="card__swoosh" viewBox="0 0 899 574" aria-hidden="true">
      <path d="M0,300 Q340,-10 895,300 Q350,40 0,312 Z" fill="var(--accent)"/>
      <path d="M0,500 Q150,500 292,452 Q140,482 0,478 Z" fill="var(--accent)"/>
    </svg>
    <div class="brand">
      <span class="brand__dot"></span>
      <span class="brand__name">
        <span class="brand__line">Corin Vale</span>
        <span class="brand__sub">Hospitality College</span>
      </span>
    </div>
    <div class="person">
      <p class="person__name">Tobin Marsh</p>
      <p class="person__role">Director</p>
    </div>
    <div class="contact contact--phones">
      <p>Phone : 1300 615 737</p>
      <p>Mobile : 0455 817 296</p>
    </div>
    <div class="contact contact--online">
      <p>Email : info@corinvale.example</p>
      <p>Website : www.corinvale.example</p>
    </div>
  </article>

  <article class="card card--small-right">
    <svg class="card__swoosh" viewBox="0 0 899 574" aria-hidden="true">
      <path d="M0,300 Q340,-10 895,300 Q350,40 0,312 Z" fill="var(--accent)"/>
      <path d="M0,500 Q150,500 292,452 Q140,482 0,478 Z" fill="var(--accent)"/>
    </svg>
    <div class="brand">
      <span class="brand__dot"></span>
      <span class="brand__name">
        <span class="brand__line">Corin Vale</span>
        <span class="brand__sub">Hospitality College</span>
      </span>
    </div>
    <div class="person">
      <p class="person__name">Tobin Marsh</p>
      <p class="person__role">Director</p>
    </div>
    <div class="contact contact--phones">
      <p>Phone : 1300 615 737</p>
      <p>Mobile : 0455 817 296</p>
    </div>
    <div class="contact contact--online">
      <p>Email : info@corinvale.example</p>
      <p>Website : www.corinvale.example</p>
    </div>
  </article>

</main>
</body>
</html>
```